Webbanner für Verkauf von Pools und Poolzubehör gesucht
Zielgruppe
Wir verkaufen Pools und Poolzubehör mit einer top Beratung zum fairen Preis.
Aufgabenstellung
Wir möchten ein Webbanner wie es bereits auf unserer Website auf der Startseite als Slider eingebaut ist (vom Format).
Es sollte wie das Bild unten sein, aber auf unsere Branche umgebaut werden (also ein total zerstörter Pool zum Beispiel oder eine üble Baustelle o. ä.)
Der Text wie im Bild unten und dann ergänzt zum Beispiel mit:
Möchten Sie das?
Bei uns gibt es Top-Beratung und hochwertige Ware zum fairen Preis.
Der Text kann auch ähnlich sein. Die Aussage, die dahinter steckt, ist wichtig.
Der Banner soll später auch in die Mails zu unserern Angeboten mit eingebaut werden.

```html
<!DOCTYPE html>
<html lang="de">
<head>
<meta charset="utf-8">
<title>Pool Profis – Webbanner</title>
<link rel="stylesheet" href="https://fonts.googleapis.com/css2?family=Anton&display=swap">
<style>
  :root {
    --page-bg: #f0eff1;
    --brand-blue: #0396cc;
    --ink-dark: #16111f;
    --ink-light: #e9dde8;
    --grass-deep: #3f6a1e;
    --grass-light: #6d9a3a;
    --pool-blue: #2a8fd0;
  }
  * { margin: 0; padding: 0; box-sizing: border-box; }
  html, body {
    width: 1200px;
    height: 480px;
    overflow: hidden;
    background: var(--page-bg);
  }
  .canvas {
    width: 1200px;
    height: 480px;
    display: flex;
    align-items: center;
  }
  .banner {
    position: relative;
    width: 1200px;
    height: 310px;
    display: flex;
    font-family: "Anton", "Impact", sans-serif;
    text-transform: none;
  }
  .banner__photo {
    position: relative;
    width: 584px;
    height: 100%;
    background:
      linear-gradient(180deg, transparent 0%, transparent 44%, rgba(255,255,255,0.55) 46%, rgba(42,143,208,0.85) 56%, rgba(190,200,150,0.9) 85%),
      linear-gradient(135deg, var(--grass-deep) 0%, var(--grass-light) 60%, var(--grass-deep) 100%);
  }
  .banner__slogan {
    position: absolute;
    left: 84px;
    top: 158px;
    font-size: 44px;
    line-height: 49px;
    color: var(--ink-light);
    letter-spacing: 0.5px;
  }
  .banner__message {
    flex: 1;
    background: var(--brand-blue);
    padding: 36px 0 0 41px;
    font-size: 45px;
    line-height: 50px;
    letter-spacing: 0.3px;
  }
  .banner__message p { white-space: nowrap; }
  .is-dark { color: var(--ink-dark); }
  .is-light { color: var(--ink-light); }
</style>
</head>
<body>
  <main class="canvas">
    <section class="banner">
      <div class="banner__photo" role="img" aria-label="Mann mit Weihnachtsmütze sitzt mit einem Bierglas in einem aufblasbaren Planschbecken auf einer Wiese">
        <p class="banner__slogan">Man(n) kann sich<br>den Pool auch<br>schön trinken!</p>
      </div>
      <div class="banner__message">
        <p class="is-dark">Wir sind die Pool Profis.</p>
        <p class="is-light">Gepflegter Badespaß zum<br>fairen Preis!</p>
        <p class="is-dark">Bei uns gibt es Top-Beratung<br>und hochwertige Ware.</p>
      </div>
    </section>
  </main>
</body>
</html>
```